New Website for Futsal Competition

An existing indoor soccer competition needs a new website design http://www.brindlecourtleague.com.au/

They need a homepage and a content page designed

Target Market(s)

Males aged 20-35 typically

Number of Pages Required

2 pages

Requirements
Must have
• must have large ''Register Now'' button on the website

• Must keep with a soccer theme

• must have a feed of latest soccer new on the site but not too prominant

• Stick wity the oclour theme
Nice to have
• Looking for a high quality website design

• Some sort of image scroll...

```html
<!DOCTYPE html>
<html lang="en">
<head>
<meta charset="utf-8">
<title>Brindle Court League – Website Design</title>
<link href="https://fonts.googleapis.com/css2?family=Anton&family=Nunito:wght@400;700&family=Roboto+Condensed:wght@400;700&family=Tinos:wght@700&display=swap" rel="stylesheet">
<style>
:root{
  --night:#0d0f14;
  --grass:#8fd14f;
  --grass-deep:#3f9a2a;
  --nav:#1d86c6;
  --nav-active:#222;
  --panel:#5a74b2;
  --panel-deep:#4a62a0;
  --panel-edge:#2d4a8e;
  --title:#2e5aa8;
  --news-red:#c8102e;
  --body:#555;
  --green-box:#1f8a35;
  --green-box-2:#36b24a;
  --lime:#c6e02a;
  --gold-head:#ddb52c;
  --gold-row:#f3df45;
  --gold-text:#a98d1c;
  --footer:#6f90c8;
}
*{box-sizing:border-box;margin:0;padding:0}
html,body{width:1200px;height:2646px;overflow:hidden;background:#fff}
body{position:relative;font-family:"Nunito",sans-serif;color:var(--body)}
.page{position:absolute;left:0;width:1200px;height:1313px;overflow:hidden;background:#fff}
.page--home{top:0}
.page--results{top:1333px}
.hero-photo{position:absolute;left:0;top:0;width:1200px;height:270px;background:radial-gradient(ellipse at 52% 40%,#8a8c92 0%,#3b3d44 30%,var(--night) 70%)}
.header-wave{position:absolute;left:0;top:0}
.utility-icons{position:absolute;left:26px;top:16px;display:flex;gap:20px}
.utility-icons span{display:block;width:18px;height:14px;border:2px solid #fff;border-radius:2px}
.brand{position:absolute;left:183px;top:20px;width:224px;height:228px;background:#fff;border-radius:14px;box-shadow:0 2px 6px rgba(0,0,0,.4);display:flex;flex-direction:column;align-items:center;justify-content:center;gap:14px}
.brand-dot{width:120px;height:120px;border-radius:50%;background:var(--grass-deep)}
.brand-name{font-family:"Nunito",sans-serif;font-weight:700;font-size:19px;color:var(--grass-deep);text-align:center;line-height:1.1}
.nav-main{position:absolute;left:43px;top:310px;font-family:"Roboto Condensed",sans-serif;font-size:21px;color:var(--nav);white-space:nowrap}
.nav-sub{position:absolute;left:423px;top:400px;font-family:"Roboto Condensed",sans-serif;font-size:21px;color:var(--nav);white-space:nowrap}
.nav-main a,.nav-sub a{color:var(--nav);text-decoration:none}
.nav-main .sep{margin:0 17px;color:var(--nav)}
.nav-sub .sep{margin:0 12px;color:var(--nav)}
.nav-main a.is-active{color:var(--nav-active)}
.register{position:absolute;left:12px;top:485px;width:380px;height:148px}
.register-crowd{position:absolute;inset:0 0 22px 0;background:linear-gradient(#1a1a1a,#000);border-radius:10px 10px 0 0}
.register-word{position:absolute;left:0;right:0;top:18px;text-align:center;font-family:"Anton",sans-serif;font-size:68px;line-height:1;color:#e3121d;letter-spacing:1px}
.register-now{position:absolute;left:20px;right:20px;bottom:0;height:40px;border-radius:0 0 60% 60%/0 0 100% 100%;background:linear-gradient(#0d4f7c,#2aa0cf);text-align:center;font-family:"Roboto Condensed",sans-serif;font-style:italic;font-size:29px;line-height:40px;color:#fff}
.news{position:absolute;left:22px;top:672px;width:370px;border-left:2px solid #bbb;padding-left:22px;height:285px}
.news h2{font-family:"Anton",sans-serif;font-weight:400;font-size:21px;color:#222;line-height:1.1}
.news h2 em{font-style:normal;color:var(--news-red)}
.news h3{font-size:18px;font-weight:700;color:var(--news-red);margin-bottom:2px}
.news li{list-style:none;font-size:16px;line-height:21.7px;padding-left:12px;position:relative}
.news li::before{content:"›";position:absolute;left:0;top:-1px;color:#333;font-weight:700}
.cta-button{position:absolute;left:136px;top:942px;width:164px;height:36px;border-radius:18px;background:linear-gradient(90deg,#d42a2a 62%,#444 62%);border:2px solid #bbb;font-size:15px;color:#fff;line-height:32px;padding-left:10px;text-decoration:none}
.cta-button::after{content:"";position:absolute;right:18px;top:9px;width:14px;height:14px;border-radius:50%;background:#ddd}
.sale{position:absolute;left:15px;top:987px;width:365px;height:247px;border-radius:18px;background:linear-gradient(var(--green-box-2),var(--green-box));box-shadow:0 2px 4px rgba(0,0,0,.3)}
.sale h2{position:absolute;left:66px;top:12px;font-family:"Anton",sans-serif;font-weight:400;font-size:30px;color:#fff}
.sale-offer{position:absolute;left:20px;top:55px;width:340px;height:108px;border-radius:22px;background:linear-gradient(90deg,#e8e8e8 20%,var(--lime) 45%,#4aa62c);border:3px solid #1c6c2a}
.sale-offer .shoe{position:absolute;left:4px;top:6px;width:80px;height:92px;border-radius:50%;background:radial-gradient(circle at 40% 40%,#fff,#777)}
.sale-price{position:absolute;left:98px;top:20px;font-family:"Anton",sans-serif;font-size:34px;color:#f5f0b0;line-height:1}
.sale-more{position:absolute;left:96px;top:62px;font-family:"Anton",sans-serif;font-size:19px;color:#fff}
.sale-text{position:absolute;left:31px;top:177px;color:#fff;font-size:16px;line-height:21px}
.sale-text strong{font-size:18px}
.panel{position:absolute;left:400px;top:485px;width:791px;height:757px;border-radius:14px;background:linear-gradient(var(--panel) 0%,var(--panel-deep) 85%,#8ea4d2 100%);border:2px solid var(--panel-edge);overflow:hidden}
.panel-title{height:50px;background:linear-gradient(#fff,#dfe6f4);border-radius:12px 12px 0 0;border-bottom:2px solid var(--panel-edge);font-family:"Nunito",sans-serif;font-weight:400;font-size:28px;line-height:50px;color:var(--title);padding-left:22px;letter-spacing:.3px;white-space:nowrap;overflow:hidden}
.panel-title--long{font-size:24px;letter-spacing:0;padding-left:20px}
.stadium{position:absolute;left:8px;top:70px;width:775px;height:150px;background:linear-gradient(#3e4c8a 0%,#c8b23c 45%,#d2c448 60%,#9fc7e0 100%)}
.panel-copy{position:absolute;left:17px;top:245px;right:14px;color:#fff;font-size:15px;line-height:18.6px}
.panel-copy p{margin-bottom:18px}
.panel-copy .lead{font-weight:700}
.panel-copy ul{list-style:none;margin-bottom:18px}
.panel-copy li{padding-left:20px}
.panel-copy li.wrap{padding-left:0;text-indent:20px}
.panel-copy .call{font-size:21px;font-weight:700}
.results-copy{position:absolute;left:17px;top:66px;right:40px;color:#fff;font-weight:700;font-size:15px}
.results-copy p{margin-bottom:16px}
.league-name{font-size:15px;letter-spacing:.3px;margin-bottom:6px}
.ladder{width:738px;border-collapse:collapse;margin-left:-2px;margin-bottom:8px;font-family:"Tinos",serif;font-size:13px}
.ladder th{background:var(--gold-head);color:#5a4a10;height:46px;border:1px solid #fff;width:50%}
.ladder td{background:var(--gold-row);color:var(--gold-text);height:47px;text-align:center;border:1px solid #fff}
.scrollbar{position:absolute;right:4px;top:56px;width:12px;bottom:4px;background:#e6e9f2;border-left:1px solid #aab}
.scrollbar span{position:absolute;left:1px;right:1px;top:14px;height:220px;background:#c9cfe0;border:1px solid #99a}
.footer{position:absolute;left:0;top:1254px;width:1200px;height:59px;background:linear-gradient(var(--footer),#4f72b6);color:#fff;font-size:14px;line-height:18px}
.footer .legal{position:absolute;left:12px;top:14px}
.footer .copyright{position:absolute;right:10px;top:12px;text-align:right}
</style>
</head>
<body>

<section class="page page--home">
  <div class="hero-photo" role="img" aria-label="Night-time photo collage of futsal players in red kits striking a ball"></div>
  <svg class="header-wave" width="1200" height="480" viewBox="0 0 1200 480" aria-hidden="true">
    <defs>
      <linearGradient id="grass-a" x1="0" y1="0" x2="0" y2="1">
        <stop offset="0" stop-color="#a5db6a"/><stop offset=".55" stop-color="#e8f6dc"/><stop offset="1" stop-color="#ffffff"/>
      </linearGradient>
      <linearGradient id="sky-a" x1="0" y1="0" x2="1" y2="0">
        <stop offset="0" stop-color="#4f8ac8"/><stop offset=".5" stop-color="#bcd8f0"/><stop offset="1" stop-color="#4f8ac8"/>
      </linearGradient>
    </defs>
    <path d="M0 205 C250 250 600 250 900 215 C1050 195 1150 190 1200 200 L1200 440 C900 360 450 380 0 480 Z" fill="url(#grass-a)"/>
    <path d="M0 205 C250 250 600 250 900 215 C1050 195 1150 190 1200 200" fill="none" stroke="#6fbf3a" stroke-width="5"/>
    <path d="M330 440 C600 380 900 380 1200 445 L1200 470 C900 410 600 410 330 440 Z" fill="url(#sky-a)" opacity=".8"/>
  </svg>
  <div class="utility-icons" aria-hidden="true"><span></span><span></span><span></span></div>
  <div class="brand"><div class="brand-dot"></div><div class="brand-name">Brindle Court League</div></div>
  <nav class="nav-main">
    <a class="is-active" href="#">About Us</a><span class="sep">|</span><a href="#">Online Store</a><span class="sep">|</span><a href="#">Fixtures</a><span class="sep">|</span><a href="#">Results &amp; Ladders</a><span class="sep">|</span><a href="#">Registration &amp; Fees</a><span class="sep">|</span><a href="#">Junior’s League</a><span class="sep">|</span><a href="#">Profile</a><span class="sep">|</span><a href="#">Contact Us</a>
  </nav>
  <nav class="nav-sub">
    <a href="#">Futsal Rules</a><span class="sep">|</span><a href="#">Photos &amp; Videos</a><span class="sep">|</span><a href="#">Online Game</a><span class="sep">|</span><a href="#">Community Supports</a><span class="sep">|</span><a href="#">Employment</a>
  </nav>

  <a class="register" href="#">
    <div class="register-crowd" role="img" aria-label="Silhouette of a cheering crowd"></div>
    <div class="register-word">REGISTER</div>
    <div class="register-now">NOW</div>
  </a>
  <aside class="news">
    <h2><em>NEWS</em> AND EVENTS</h2>
    <h3>This is sample text</h3>
    <ul>
      <li>This is sample text, only intended.</li><li>This is sample text.</li>
      <li>This is sample text, only intended.</li><li>This is sample text.</li>
      <li>This is sample text, only intended.</li><li>This is sample text.</li>
      <li>This is sample text, only intended.</li><li>This is sample text.</li>
      <li>This is sample text, only intended.</li><li>This is sample text.</li>
    </ul>
  </aside>
  <a class="cta-button" href="#">Click Here</a>
  <div class="sale">
    <h2>FOR SALE !!!</h2>
    <div class="sale-offer"><div class="shoe" role="img" aria-label="Futsal boot and ball"></div><div class="sale-price">$99.90</div><div class="sale-more">SEE MORE</div></div>
    <div class="sale-text"><strong>This is sample text</strong><br>This is sample text, only intended.<br>This is sample text.</div>
  </div>

  <main class="panel">
    <h1 class="panel-title">FUTSAL INDOOR SOCCER IN MELBOURNE</h1>
    <div class="stadium" role="img" aria-label="Panorama of a packed indoor futsal arena"></div>
    <div class="panel-copy">
      <p class="lead">Brindle Court League offers people of all ages who love the excitement of soccer, a chance to play THE WORLD GAME in an indoor environment for fitness and fun all year round.</p>
      <p>Whether you are looking for competition, or just fun, indoor soccer, otherwise known as futsal, is a great way to stay fit and test your skills in an all weather venue. Form a team or just register your interest to join one at one of our venues. Indoor soccer (futsal) is a great social sport for competitors and spectators.</p>
      <p>So what are you waiting for? With futsal centres located in Northgate, Bayview, Westmere &amp; Hillcrest, their is sure to be an indoor soccer venue near you.</p>
      <p>Some more reasons to play indoor soccer (futsal) at one of our venues:</p>
      <ul>
        <li>* It’s easy to form a team with a minimum of only 5 players required</li>
        <li>* Great way to socialise with friends and remain fit at the same time</li>
        <li>* Choose from Men’s, Women’s and Mixed Indoor Soccer Leagues</li>
        <li>* Junior Indoor Soccer Leagues (Under 16’s)</li>
        <li>* Finals series Trophies presentations and awards</li>
        <li class="wrap">* Qualified and experienced indoor soccer referees. All our referees have completed a Level 5 Futsal Referee Training course from the State Futsal Association</li>
        <li>* Public liability abd personal indemnity insurance through Australia’s largest sports insurance companies</li>
        <li>* Four convenient locations: Northgate, Bayview, Westmere and Hillcrest</li>
      </ul>
      <p class="call">Call us today on 0400 555 123 to register your interest</p>
    </div>
  </main>

  <footer class="footer">
    <div class="legal">Privacy Policy<br>Terms &amp; Conditions</div>
    <div class="copyright">Copyright © 2004 CompanyName.<br>All Rights Reserved.</div>
  </footer>
</section>

<section class="page page--results">
  <div class="hero-photo" role="img" aria-label="Night-time photo collage of futsal players in red kits striking a ball"></div>
  <svg class="header-wave" width="1200" height="480" viewBox="0 0 1200 480" aria-hidden="true">
    <defs>
      <linearGradient id="grass-b" x1="0" y1="0" x2="0" y2="1">
        <stop offset="0" stop-color="#a5db6a"/><stop offset=".55" stop-color="#e8f6dc"/><stop offset="1" stop-color="#ffffff"/>
      </linearGradient>
      <linearGradient id="sky-b" x1="0" y1="0" x2="1" y2="0">
        <stop offset="0" stop-color="#4f8ac8"/><stop offset=".5" stop-color="#bcd8f0"/><stop offset="1" stop-color="#4f8ac8"/>
      </linearGradient>
    </defs>
    <path d="M0 205 C250 250 600 250 900 215 C1050 195 1150 190 1200 200 L1200 440 C900 360 450 380 0 480 Z" fill="url(#grass-b)"/>
    <path d="M0 205 C250 250 600 250 900 215 C1050 195 1150 190 1200 200" fill="none" stroke="#6fbf3a" stroke-width="5"/>
    <path d="M330 440 C600 380 900 380 1200 445 L1200 470 C900 410 600 410 330 440 Z" fill="url(#sky-b)" opacity=".8"/>
  </svg>
  <div class="utility-icons" aria-hidden="true"><span></span><span></span><span></span></div>
  <div class="brand"><div class="brand-dot"></div><div class="brand-name">Brindle Court League</div></div>
  <nav class="nav-main">
    <a href="#">About Us</a><span class="sep">|</span><a href="#">Online Store</a><span class="sep">|</span><a href="#">Fixtures</a><span class="sep">|</span><a class="is-active" href="#">Results &amp; Ladders</a><span class="sep">|</span><a href="#">Registration &amp; Fees</a><span class="sep">|</span><a href="#">Junior’s League</a><span class="sep">|</span><a href="#">Profile</a><span class="sep">|</span><a href="#">Contact Us</a>
  </nav>
  <nav class="nav-sub">
    <a href="#">Futsal Rules</a><span class="sep">|</span><a href="#">Photos &amp; Videos</a><span class="sep">|</span><a href="#">Online Game</a><span class="sep">|</span><a href="#">Community Supports</a><span class="sep">|</span><a href="#">Employment</a>
  </nav>

  <a class="register" href="#">
    <div class="register-crowd" role="img" aria-label="Silhouette of a cheering crowd"></div>
    <div class="register-word">REGISTER</div>
    <div class="register-now">NOW</div>
  </a>
  <aside class="news">
    <h2><em>NEWS</em> AND EVENTS</h2>
    <h3>This is sample text</h3>
    <ul>
      <li>This is sample text, only intended.</li><li>This is sample text.</li>
      <li>This is sample text, only intended.</li><li>This is sample text.</li>
      <li>This is sample text, only intended.</li><li>This is sample text.</li>
      <li>This is sample text, only intended.</li><li>This is sample text.</li>
      <li>This is sample text, only intended.</li><li>This is sample text.</li>
    </ul>
  </aside>
  <a class="cta-button" href="#">Click Here</a>
  <div class="sale">
    <h2>FOR SALE !!!</h2>
    <div class="sale-offer"><div class="shoe" role="img" aria-label="Futsal boot and ball"></div><div class="sale-price">$99.90</div><div class="sale-more">SEE MORE</div></div>
    <div class="sale-text"><strong>This is sample text</strong><br>This is sample text, only intended.<br>This is sample text.</div>
  </div>

  <main class="panel">
    <h1 class="panel-title panel-title--long">RESULTS and LADDERS – INDOOR SOCCER IN MELBOURNE</h1>
    <div class="scrollbar" aria-hidden="true"><span></span></div>
    <div class="results-copy">
      <p>Click the links below to view the old indoor soccer season's fixture for your league.</p>
      <p>The ladders and fixture are both updated with results for all games as they are played.</p>
      <h2 class="league-name">WESTMERE INDOOR SOCCER LEAGUE</h2>
      <table class="ladder">
        <tr><th>INDOOR SOCCER LEAGUE LADDERS</th><th>INDOOR SOCCER RESULTS</th></tr>
        <tr><td>Monday Mixed League</td><td>Monday Mixed League</td></tr>
        <tr><td>Tuesday Men's League</td><td>Tuesday Men's League</td></tr>
        <tr><td>Wednesday Men's League</td><td>Wednesday Men's League</td></tr>
        <tr><td>Thursday Men's League</td><td>Thursday Men's League</td></tr>
        <tr><td>Friday Juniors League</td><td>Friday Juniors League</td></tr>
      </table>
      <h2 class="league-name">BAYVIEW INDOOR SOCCER LEAGUE</h2>
      <table class="ladder">
        <tr><th>INDOOR SOCCER LEAGUE LADDERS</th><th>INDOOR SOCCER RESULTS</th></tr>
        <tr><td>Monday Men's League</td><td>Monday Men's League</td></tr>
        <tr><td>Wednesday Men's League</td><td>Wednesday Men's League</td></tr>
      </table>
      <h2 class="league-name">NORTHGATE INDOOR SOCCER LEAGUE</h2>
      <table class="ladder">
        <tr><th>INDOOR SOCCER LEAGUE LADDERS</th><th>INDOOR SOCCER RESULTS</th></tr>
        <tr><td>Friday Men's League</td><td>Friday Men's League</td></tr>
      </table>
    </div>
  </main>

  <footer class="footer">
    <div class="legal">Privacy Policy<br>Terms &amp; Conditions</div>
    <div class="copyright">Copyright © 2004 CompanyName.<br>All Rights Reserved.</div>
  </footer>
</section>

</body>
</html>
```